Landing page for Brook Aerowing

Re-design the landing page for www.brookaerowing.example. It needs to be flatter and work with both PC, Mac and Mobile. Sites I like are as follows:
http://tarnelflight.example
http://qoskyway.example
http://www.velmoplanes.example
http://www.dunmorewing.example/dmw.php
http://www.ulvane.example
http://www.cedrolskies.example
http://www.pembrookflighthub.example
http://www.corvallowings.example
http://www.tessorivawings.example

We are a Marlow 48 Dealer, SkyNoble FBO member, Vortell Circle FBO, QMR Preferred FBO located only 6 miles from Downtown Atlanta. Providing Aircraft charter, Aircraft sales, Aircraft Maintenance, Aircraft Line Services and Hangar, and Parts Support.

Reason: I have six people reviewing designs within the company and will not be able to complete the review until next week.

Target Market(s)

Pilot's looking for a place to take care of them in Atlanta

Industry/Entity Type

Group

Colors
fbed22
0555a3

Requirements
Must have
• Slogan "Focused on Arrival" and "Sensational Southern Service"

```html
<!DOCTYPE html>
<html lang="en">
<head>
<meta charset="utf-8">
<title>Brook Aerowing — Landing Page</title>
<link rel="stylesheet" href="https://fonts.googleapis.com/css2?family=Arimo:wght@400;700&display=swap">
<style>
  :root {
    --brand-yellow: #fbed22;
    --brand-blue: #0555a3;
    --link-blue: #2a6fb5;
    --nav-text: #39a6e6;
    --ink: #222222;
    --muted: #6b6b6b;
    --soft: #8a8a8a;
    --intro-bg: #f7f7f7;
    --grid-bg: #e4e4e4;
    --band-white: #ffffff;
    --night: #000000;
    --footer-text: #5e5e5e;
    --rule: #d2d2d2;
  }
  * { box-sizing: border-box; margin: 0; padding: 0; }
  html, body { width: 1200px; height: 1159px; overflow: hidden; }
  body { position: relative; font-family: "Arimo", Arial, sans-serif; color: var(--ink); background: var(--band-white); }
  .abs { position: absolute; }

  /* Hero */
  .hero { left: 0; top: 0; width: 1200px; height: 285px;
    background:
      radial-gradient(ellipse 420px 110px at 560px 150px, rgba(225,228,236,.55), rgba(225,228,236,0) 70%),
      linear-gradient(180deg, #06133f 0%, #0c2a78 42%, #1d4396 62%, #3a3f52 72%, #2a2622 82%, #121212 100%); }
  .brand-mark { left: 257px; top: 24px; display: flex; align-items: center; gap: 6px;
    font-size: 15px; font-weight: 700; color: var(--brand-yellow); }
  .brand-mark .square { width: 12px; height: 12px; background: var(--brand-yellow); }
  .brand-slogan { left: 275px; top: 44px; font-size: 9px; color: #ffffff; letter-spacing: .3px; }
  .clock-bar { left: 255px; top: 254px; width: 685px; height: 31px; background: rgba(232,226,40,.86); }
  .clock { top: 267px; font-size: 7px; color: #1b1b1b; }

  /* Navigation */
  .nav { left: 0; top: 285px; width: 1200px; height: 44px; background: var(--night); }
  .nav-active { left: 255px; top: 285px; width: 59px; height: 44px; background: var(--brand-blue); }
  .nav-item { top: 304px; font-size: 10px; color: var(--nav-text); white-space: nowrap; }
  .nav-item.is-active { color: #ffffff; }

  /* Intro */
  .intro { left: 0; top: 329px; width: 1200px; height: 218px; background: var(--intro-bg); }
  .intro-divider { left: 481px; top: 362px; width: 1px; height: 162px; background: var(--rule); }
  .intro-heading { top: 362px; font-size: 10.5px; color: var(--ink); font-weight: 400; }
  .intro-lead { left: 255px; top: 396px; width: 200px; font-size: 7.5px; line-height: 10px; color: var(--muted); }
  .intro-slogan { left: 255px; top: 424px; font-size: 7.5px; color: var(--muted); }
  .intro-slogan em { font-style: normal; font-size: 10px; color: var(--brand-blue); }
  .welcome-news { left: 527px; top: 392px; width: 360px; font-size: 10.5px; line-height: 14px; color: var(--muted); }
  .welcome-body { left: 527px; top: 435px; width: 405px; font-size: 7px; line-height: 9.5px; color: var(--soft); }
  .welcome-body p + p { margin-top: 9px; }

  /* Services grid */
  .services { left: 0; top: 547px; width: 1200px; height: 418px; background: var(--grid-bg); }
  .card { width: 213px; }
  .card-photo { width: 213px; height: 109px; border: 4px solid #ffffff; }
  .card-title { margin-top: 10px; font-size: 9.5px; line-height: 11px; color: var(--link-blue); text-transform: uppercase; font-weight: 400; }
  .card-text { margin-top: 4px; font-size: 7.3px; line-height: 9.5px; color: var(--soft); }
  .card-more { position: absolute; top: 162px; font-size: 7px; color: var(--ink); }
  .card-plus { position: absolute; right: 4px; top: 81px; width: 24px; height: 24px; background: var(--brand-yellow);
    display: flex; align-items: center; justify-content: center; }

  /* Partners */
  .partners { left: 0; top: 965px; width: 1200px; height: 59px; background: var(--band-white); }

  /* Footer */
  .footer { left: 0; top: 1024px; width: 1200px; height: 135px; background: var(--night); }
  .footer-brand { left: 257px; top: 1074px; display: flex; align-items: center; gap: 6px;
    font-size: 14px; font-weight: 700; color: var(--brand-yellow); }
  .footer-brand .square { width: 11px; height: 11px; background: var(--brand-yellow); }
  .footer-copy { left: 257px; top: 1127px; font-size: 6px; color: var(--footer-text); }
  .footer-rule { top: 1062px; width: 1px; height: 90px; background: #1f1f1f; }
  .footer-col { font-size: 6.6px; line-height: 9.8px; color: var(--footer-text); }
  .footer-col .gap { height: 9px; }
</style>
</head>
<body>

<header>
  <div class="abs hero" role="img" aria-label="Night photograph of a white business jet parked on a lit airport apron"></div>
  <div class="abs brand-mark"><span class="square"></span>Brook Aerowing</div>
  <span class="abs brand-slogan">Focused on Arrival</span>

  <div class="abs clock-bar"></div>
  <span class="abs clock" style="left:284px">Atlanta - 22.00.24</span>
  <span class="abs clock" style="left:384px">GMT - 22.00.24</span>
  <span class="abs clock" style="left:471px">San Francisco - 22.00.24</span>
  <span class="abs clock" style="left:591px">Salt Lake - 22.00.24</span>
  <span class="abs clock" style="left:703px">Dallas - 22.00.24</span>
  <span class="abs clock" style="left:806px">London - 22.00.24</span>

  <nav>
    <div class="abs nav"></div>
    <div class="abs nav-active"></div>
    <span class="abs nav-item is-active" style="left:265px">About Us</span>
    <span class="abs nav-item" style="left:326px">Aircraft Management</span>
    <span class="abs nav-item" style="left:436px">Charter</span>
    <span class="abs nav-item" style="left:489px">FBO Services</span>
    <span class="abs nav-item" style="left:574px">Maintenence</span>
    <span class="abs nav-item" style="left:654px">Aircraft Parts</span>
    <span class="abs nav-item" style="left:734px">Aircraft Sales</span>
    <span class="abs nav-item" style="left:812px">Resources</span>
    <span class="abs nav-item" style="left:876px">Contact Us</span>
  </nav>
</header>

<main>
  <section>
    <div class="abs intro"></div>
    <h2 class="abs intro-heading" style="left:255px">You've landed at Brook Aerowing!</h2>
    <p class="abs intro-lead">Let Brook Aerowing show you why we have been named the #1 FBO in Georgia multiple times.</p>
    <p class="abs intro-slogan">Experience our "<em>Sensational Southern Service</em>".</p>
    <div class="abs intro-divider"></div>
    <h1 class="abs intro-heading" style="left:525px">WELCOME TO OUR WEBSITE !</h1>
    <p class="abs welcome-news">Harlan Avionics establishes Satellite Avionics Location at Brook Aerowing KBRX Location in Atlanta, Georgia.</p>
    <div class="abs welcome-body">
      <p>Atlanta's Most Established Fixed Based Operation established in 1955 by Southern Aviation Hall of Honor member Ray Brook, Sr.</p>
      <p>Our world class FBO facilities offer all the amenities for passengers and pilots, including computer work stations with internet access, plasma TV for catching up on national and world events, pilots lounge with theatre seating and security camera monitors and state of the art flight planning facilities. Our line technicians are FlightSafe First trained and Brook Aerowing is a State of Georgia recognized drug-free workplace.</p>
    </div>
  </section>

  <section>
    <div class="abs services"></div>

    <article class="abs card" style="left:255px;top:574px">
      <div class="card-photo" style="background:linear-gradient(180deg,#c9c36a,#a9a455)" role="img" aria-label="Charter jet on the ramp with yellow highlight"></div>
      <div class="card-plus"><svg width="10" height="10" viewBox="0 0 10 10"><path d="M5 1v8M1 5h8" stroke="#222" stroke-width="1.6"/></svg></div>
      <h3 class="card-title">Air Craft Charter</h3>
      <p class="card-text">Lorem ipsum dolor sit amet, consectetur adipisicing elit, sed do eiusmod tempor incididunt</p>
      <span class="card-more">MORE</span>
    </article>

    <article class="abs card" style="left:491px;top:574px">
      <div class="card-photo" style="background:linear-gradient(180deg,#5f7f9a,#3e4a55 60%,#7a7d80)" role="img" aria-label="Aircraft and tug inside a hangar"></div>
      <h3 class="card-title">Block Time &amp; Custom Innovative Ownership Programs</h3>
      <p class="card-text">Lorem ipsum dolor sit amet, consectetur adipisicing elit, sed</p>
      <span class="card-more">MORE</span>
    </article>

    <article class="abs card" style="left:727px;top:574px">
      <div class="card-photo" style="background:linear-gradient(135deg,#3a5c9a,#2a4a82 55%,#5b4a3a)" role="img" aria-label="Line technician in uniform handling fuel"></div>
      <h3 class="card-title" style="width:230px">Line Services Including Fueling &amp; Storage</h3>
      <p class="card-text">Lorem ipsum dolor sit amet, consectetur adipisicing elit, sed</p>
      <span class="card-more">MORE</span>
    </article>

    <article class="abs card" style="left:255px;top:765px">
      <div class="card-photo" style="background:linear-gradient(180deg,#6f7c94,#c9ccd2 55%,#5a5f66)" role="img" aria-label="Twin propeller aircraft in front of the hangar"></div>
      <h3 class="card-title">Air Craft Spares Support</h3>
      <p class="card-text">Lorem ipsum dolor sit amet, consectetur adipisicing elit, sed do eiusmod tempor incididunt</p>
      <span class="card-more">MORE</span>
    </article>

    <article class="abs card" style="left:491px;top:765px">
      <div class="card-photo" style="background:linear-gradient(180deg,#8d918c,#b7bbb4 50%,#6e6f6a)" role="img" aria-label="Leather seats in a jet cabin"></div>
      <h3 class="card-title">Air Craft Sales</h3>
      <p class="card-text">Lorem ipsum dolor sit amet, consectetur adipisicing elit, sed do eiusmod tempor incididunt</p>
      <span class="card-more">MORE</span>
    </article>

    <article class="abs card" style="left:727px;top:765px">
      <div class="card-photo" style="background:linear-gradient(180deg,#6f95c8,#b9cde3 55%,#6d7278)" role="img" aria-label="Light jet on an open apron under blue sky"></div>
      <h3 class="card-title">Air Craft Sales</h3>
      <p class="card-text">Lorem ipsum dolor sit amet, consectetur adipisicing elit, sed do eiusmod tempor incididunt</p>
      <span class="card-more">MORE</span>
    </article>
  </section>

  <section aria-label="Partners">
    <div class="abs partners"></div>
    <svg class="abs" style="left:0;top:965px" width="1200" height="59" viewBox="0 0 1200 59">
      <rect x="256" y="17" width="38" height="25" fill="#2c8c3a"/>
      <rect x="334" y="20" width="50" height="18" rx="9" fill="#7ab0d8"/>
      <rect x="427" y="21" width="50" height="17" fill="none" stroke="#2a4c88" stroke-width="1.5"/>
      <rect x="479" y="21" width="32" height="17" fill="#c7a54a"/>
      <rect x="550" y="23" width="50" height="12" fill="#1f2a4a"/>
      <rect x="633" y="22" width="30" height="14" fill="#1d4f9a"/>
      <rect x="703" y="25" width="28" height="8" fill="#9aa4b4"/>
      <rect x="777" y="23" width="30" height="12" fill="#d8c21a"/>
      <circle cx="852" cy="29" r="6" fill="#1c3a7a"/>
      <rect x="861" y="24" width="25" height="10" fill="#1c3a7a"/>
    </svg>
  </section>
</main>

<footer>
  <div class="abs footer"></div>
  <div class="abs footer-brand"><span class="square"></span>Brook Aerowing</div>
  <span class="abs footer-copy">©Copyright 2014 Brook Aerowing &amp; Leasing All Rights Reserved</span>

  <div class="abs footer-rule" style="left:444px"></div>
  <div class="abs footer-col" style="left:465px;top:1069px">
    Brook Aerowing and Leasing Corp.<br>120 Runway Loop<br>Atlanta, GA 30000
  </div>
  <div class="abs footer-col" style="left:593px;top:1069px">
    Phone: 404-555-0140 / 800-555-0172<br>Fax: .....404-555-0188
    <div class="gap"></div>
    Charter.......... 678-555-0113<br>Accounting .... 678-555-0117<br>Parts............ 404-555-0174<br>Maintenance.... 678-555-0100
  </div>
  <div class="abs footer-rule" style="left:744px"></div>
  <div class="abs footer-col" style="left:767px;top:1071px">
    About Us<br>Aircraft Management<br>Charter<br>FBO Services<br>Maintenance<br>Aircraft Parts<br>Aircraft Sales<br>Resources
  </div>
</footer>

</body>
</html>
```